Yacht, Boats, Watersports company needs a redesign of business card

Hello Designers!
We are a Boat dealership company that sells fun in the water, we sell boats, Yachts, Kayaks and also yacht WaterSport toys. We are looking to redesign our business cards in to something a little bit more sophisticated. in a way that we can make better use of our company colors. I'm attaching a zipped file containing the company 3 sets of company logo which one is an horizontal another one is a vertical and also a chromed 3d logo. Also is included two set of business cards that we use and also some designs that i think it's interesting. We use PMS 2026c Orange and PMS 7687C Blue. I would like to see at least two different options with the orange as accent and also using blue as an accent color. It's really important for the business cards to have a font option and size that is legible to most people. Our current website is wwww.corvellamarine.com. Please visit if you want to have a better feeling of the Boat dealership
You can send Single sided or double side options. We are now using single sided but we may be open for a double side option if we really like the design.
Target Market(s)
Marine, boat sales, yacht sales, water toys sales/
Contact Information for Business Card
Name: Dale Pritchett
Address: 718 West Halden Lane,
Dania Beach, FL 33019
Phone: 954-382-7146
Fax: 954:382-7139
Cell: 954-451-8320
Email: 212@corvellamarine.com
Website: corvellamarine.com
Requirements
Must have
- the current information of the business card provided.
logo
use the PMS Colors
Nice to have
- a touch of elegance and sophistication but simple
Should not have
- should not have any typography that is hard to read, the card should be simple but yet sophisticated.

```html
<!DOCTYPE html>
<html lang="en">
<head>
<meta charset="utf-8">
<title>Corvella Marine – Business Card</title>
<link href="https://fonts.googleapis.com/css2?family=Montserrat:wght@700&family=Questrial&display=swap" rel="stylesheet">
<style>
  :root {
    --blue: #21457f;
    --orange: #ef4d23;
    --white: #ffffff;
    --ink: #4a4a4a;
    --backdrop: #e9eaec;
  }
  html, body {
    margin: 0;
    padding: 0;
    width: 1200px;
    height: 900px;
    overflow: hidden;
    background: var(--backdrop);
  }
  .canvas {
    position: relative;
    width: 1200px;
    height: 900px;
  }
  .card {
    position: absolute;
    left: 300px;
    width: 600px;
    height: 343px;
    box-shadow: 0 6px 18px rgba(0,0,0,0.12);
  }
  .card--front { top: 88px; background: var(--blue); }
  .card--back { top: 469px; background: var(--white); }

  .brand {
    position: absolute;
    display: flex;
    align-items: center;
    gap: 14px;
    font-family: "Montserrat", sans-serif;
    font-weight: 700;
    letter-spacing: 0.08em;
    text-transform: uppercase;
    white-space: nowrap;
  }
  .brand__dot {
    width: 34px;
    height: 34px;
    border-radius: 50%;
    background: var(--orange);
    flex: none;
  }
  .card--front .brand {
    left: 50%;
    top: 50%;
    transform: translate(-50%, -50%);
    font-size: 30px;
    color: var(--white);
  }
  .card--back .brand {
    right: 38px;
    top: 70px;
    font-size: 19px;
    color: var(--blue);
    gap: 10px;
  }
  .card--back .brand .brand__dot { width: 24px; height: 24px; }

  .contact {
    position: absolute;
    left: 0;
    top: 128px;
    font-family: "Questrial", sans-serif;
    color: var(--ink);
  }
  .contact__name {
    display: flex;
    align-items: center;
    margin: 0;
    font-family: "Montserrat", sans-serif;
    font-weight: 700;
    font-size: 26px;
    letter-spacing: 0.04em;
    text-transform: uppercase;
    color: var(--blue);
  }
  .contact__marker {
    width: 14px;
    height: 30px;
    background: var(--blue);
    margin-right: 28px;
  }
  .contact__surname { color: var(--orange); margin-left: 10px; }
  .contact__address {
    margin: 14px 0 0 42px;
    font-size: 14px;
    line-height: 1.35;
  }
  .contact__list {
    list-style: none;
    margin: 18px 0 0 42px;
    padding: 0;
    font-size: 14px;
    line-height: 1.45;
  }
  .contact__list li { display: flex; align-items: center; gap: 8px; }
  .contact__list svg { width: 11px; height: 11px; fill: var(--orange); flex: none; }
</style>
</head>
<body>
<main class="canvas">
  <section class="card card--front" aria-label="Card front">
    <div class="brand">
      <span class="brand__dot"></span>
      <span class="brand__name">Corvella Marine</span>
    </div>
  </section>

  <section class="card card--back" aria-label="Card back">
    <div class="brand">
      <span class="brand__dot"></span>
      <span class="brand__name">Corvella Marine</span>
    </div>

    <div class="contact">
      <h1 class="contact__name"><span class="contact__marker"></span>Dale<span class="contact__surname">Pritchett</span></h1>
      <p class="contact__address">718 West Halden Lane,<br>Dania Beach, FL 33019</p>
      <ul class="contact__list">
        <li><svg viewBox="0 0 12 12" aria-hidden="true"><path d="M3 0h6a1 1 0 0 1 1 1v10a1 1 0 0 1-1 1H3a1 1 0 0 1-1-1V1a1 1 0 0 1 1-1zm0 2v7h6V2z"/></svg>954-382-7146</li>
        <li><svg viewBox="0 0 12 12" aria-hidden="true"><path d="M2.5 1l2 2.5-1.2 1.3a7 7 0 0 0 3.9 3.9L8.5 7.5 11 9.5 9.8 11.2C5 11 1 7 .8 2.2z"/></svg>954-451-8320</li>
        <li><svg viewBox="0 0 12 12" aria-hidden="true"><path d="M3 0h6v3H3zM1 4h10v5H9v3H3V9H1zm3 4v3h4V8z"/></svg>954:382-7139</li>
        <li><svg viewBox="0 0 12 12" aria-hidden="true"><path d="M0 2h12v8H0zm1 1v.4l5 3.3 5-3.3V3z"/></svg>212@corvellamarine.com</li>
        <li><svg viewBox="0 0 12 12" aria-hidden="true"><path d="M6 0a6 6 0 1 1 0 12A6 6 0 0 1 6 0zm-2 2.5L2.5 5 4 6.5 5.5 6 7 8v2.5A4.8 4.8 0 0 0 10.7 6H9L7.5 4.5 8 2a4.8 4.8 0 0 0-4 .5z"/></svg>www.corvellamarine.com</li>
      </ul>
    </div>
  </section>
</main>
</body>
</html>
```